TORRENT DYNAMICS CUSTOM MARINE AUDIO

TORRENT DYNAMICS IS A CUSTOM MARINE AUDIO SHOP. NEED A FLIER THAT HAS SOME OF THE BRANDS WE INSTALL, MY SHOP LOGO AND BUSINESS INFO. I WILL ATTACH THE LOGOS I HAVE. SOME ARE NOT HIGH QUALITY THOUGH. I WILL ALSO ATTACH SOME PICS OF OUR INSTALLS THAT MIGHT CAN BE USED. SHOP INFORMATION:TORRENT DYNAMICS LLC20 E CHICKASAW AVEMCALESTER, OK 74501918-470-7011

Target Market(s)

MARINE AUDIO

Industry/Entity Type

Audio

Font styles to use
Decorative

Colors

Designer to choose colors to be used in the design.

Requirements
Must have
• BRAND LOGOS
• TORRENT LOGO

```html
<!DOCTYPE html>
<html lang="en">
<head>
<meta charset="utf-8">
<title>Torrent Dynamics – Custom Marine Audio Flyer</title>
<link rel="stylesheet" href="https://fonts.googleapis.com/css2?family=Audiowide&family=Open+Sans:ital,wght@0,400;0,600;1,400;1,600;1,700&display=swap">
<style>
  :root {
    --royal: #2c3282;
    --royal-deep: #232870;
    --charcoal: #1a1a1a;
    --graphite: #3a3a3a;
    --mist: #eeeeef;
    --paper: #ffffff;
    --ink: #333333;
    --steel: #8a8a8a;
    --backdrop: #d9d9d9;
  }
  * { margin: 0; padding: 0; box-sizing: border-box; }
  html, body { width: 1026px; height: 1200px; overflow: hidden; background: var(--backdrop); }
  .canvas { position: relative; width: 1026px; height: 1200px; }
  .flyer {
    position: absolute; left: 46px; top: 0;
    width: 876px; height: 1125px;
    transform: scale(1.0667); transform-origin: top left;
    background: var(--mist);
    overflow: hidden;
    font-family: "Open Sans", sans-serif;
  }
  .artwork { position: absolute; left: 0; top: 0; width: 876px; height: 1125px; }
  .brand-name {
    position: absolute; left: 230px; top: 560px; width: 420px;
    text-align: center; color: var(--royal);
    font-family: "Audiowide", sans-serif; line-height: 1;
  }
  .brand-name .word-main { display: block; font-size: 60px; letter-spacing: 2px; }
  .brand-name .word-sub { display: block; font-size: 17px; letter-spacing: 9px; margin-top: 4px; }
  .shop-title {
    position: absolute; left: 28px; top: 722px;
    font-family: "Audiowide", sans-serif; font-style: italic;
    font-size: 46px; line-height: 62px; color: var(--paper);
  }
  .shop-intro {
    position: absolute; left: 30px; top: 865px; width: 360px;
    font-style: italic; font-size: 26px; line-height: 35px; color: #e4e4e4;
  }
  .estimate {
    position: absolute; right: 30px; top: 720px;
    font-family: "Audiowide", sans-serif; font-style: italic;
    font-size: 36px; color: var(--paper);
  }
  .phone {
    position: absolute; right: 28px; top: 786px;
    display: flex; align-items: center; gap: 20px;
    font-size: 29px; color: var(--paper);
  }
  .address {
    position: absolute; right: 30px; top: 866px; text-align: right;
    font-size: 22px; line-height: 30px; color: var(--ink);
  }
  .address svg { vertical-align: -2px; margin-right: 6px; }
  .tagline {
    position: absolute; right: 26px; top: 951px; text-align: right;
    font-style: italic; font-weight: 700; font-size: 18px; line-height: 25px;
    color: var(--royal); text-transform: uppercase;
  }
  .partners {
    position: absolute; left: 0; top: 1030px; width: 876px; height: 95px;
    background: var(--paper);
    display: flex; align-items: center; justify-content: space-around; padding: 0 12px;
    color: #6e6e6e;
  }
  .partner { display: flex; align-items: center; gap: 8px; font-weight: 600; }
  .partner small { display: block; font-weight: 400; font-size: 13px; letter-spacing: 2px; }
  .partner-mark { width: 34px; height: 34px; background: #7a7a7a; transform: rotate(45deg); }
</style>
</head>
<body>
<div class="canvas">
  <div class="flyer">
    <svg class="artwork" viewBox="0 0 876 1125" xmlns="http://www.w3.org/2000/svg">
      <defs>
        <linearGradient id="sunset" x1="0" y1="0" x2="0" y2="1">
          <stop offset="0" stop-color="#1c2240"/><stop offset="0.45" stop-color="#d99a6a"/><stop offset="0.6" stop-color="#3a4660"/><stop offset="1" stop-color="#141a3a"/>
        </linearGradient>
        <linearGradient id="pontoon" x1="0" y1="0" x2="0" y2="1">
          <stop offset="0" stop-color="#8fb8e6"/><stop offset="0.5" stop-color="#8a2a30"/><stop offset="1" stop-color="#9aa3ad"/>
        </linearGradient>
        <linearGradient id="deck" x1="0" y1="0" x2="0" y2="1">
          <stop offset="0" stop-color="#2e4a4a"/><stop offset="0.5" stop-color="#d8dde2"/><stop offset="1" stop-color="#3a3530"/>
        </linearGradient>
        <radialGradient id="shade" cx="0.5" cy="0.5" r="0.7">
          <stop offset="0" stop-color="#5a5a5a"/><stop offset="1" stop-color="#111"/>
        </radialGradient>
      </defs>
      <polygon points="0,0 310,0 0,295" fill="var(--royal)"/>
      <polygon points="580,0 876,0 876,320" fill="url(#shade)"/>
      <polygon points="0,540 0,640 140,640" fill="url(#shade)"/>
      <polygon points="876,505 876,640 730,640" fill="var(--royal)"/>
      <polygon role="img" aria-label="Photo: boat tower speakers with blue lighting over a lake at sunset" points="310,0 555,0 680,125 435,380 185,125" fill="url(#sunset)"/>
      <polygon role="img" aria-label="Photo: red pontoon boat with tower speaker array under blue sky" points="180,150 420,395 185,640 0,640 0,295" fill="url(#pontoon)"/>
      <polygon role="img" aria-label="Photo: wake boat interior with green-lit tower speakers and white seating" points="695,150 876,330 876,500 735,640 690,640 455,400" fill="url(#deck)"/>
      <polygon points="0,680 390,680 550,1030 0,1030" fill="url(#shade)"/>
      <polygon points="410,680 876,680 876,848 490,848" fill="var(--royal)"/>
    </svg>

    <div class="brand-name"><span class="word-main">TORRENT</span><span class="word-sub">DYNAMICS</span></div>

    <h1 class="shop-title">MARINE<br>AUDIO SHOP</h1>
    <p class="shop-intro">We offer customized audio installation at our store or at your home or dock.</p>

    <p class="estimate">FREE ESTIMATE!</p>
    <p class="phone">
      <svg width="32" height="32" viewBox="0 0 32 32" aria-hidden="true"><circle cx="16" cy="16" r="14" fill="none" stroke="#fff" stroke-width="2.5"/><path d="M11 9c1-1 2-1 2.6 0l1.4 2.4c.4.8.2 1.4-.5 2l-1 .8c.8 2 2.3 3.5 4.3 4.3l.8-1c.6-.7 1.2-.9 2-.5l2.4 1.4c1 .6 1 1.6 0 2.6-1.4 1.4-3.2 1.6-5.6.2-3-1.8-5-3.8-6.8-6.8C9.4 12.2 9.6 10.4 11 9z" fill="#fff"/></svg>
      918-555-0163
    </p>
    <p class="address">
      <svg width="14" height="20" viewBox="0 0 14 20" aria-hidden="true"><path d="M7 0a7 7 0 0 1 7 7c0 5-7 13-7 13S0 12 0 7a7 7 0 0 1 7-7z" fill="#666"/><circle cx="7" cy="7" r="2.6" fill="#eee"/></svg>47 W Brindlewood Ave,<br>Granville, Oklahoma, OK
    </p>
    <p class="tagline">Designed for the harshest<br>marine environment.</p>

    <div class="partners">
      <div class="partner"><span class="partner-mark"></span></div>
      <div class="partner"><div style="font-size:22px">Harborline<small>MARINE AUDIO</small></div></div>
      <div class="partner"><div style="font-size:18px">Tidewater<small>audio</small></div></div>
      <div class="partner"><span class="partner-mark"></span><span style="font-size:26px">KEELFORM</span></div>
      <div class="partner"><div style="font-size:18px;text-align:center">Northwake Audio<small>tuned for water</small></div></div>
    </div>
  </div>
</div>
</body>
</html>
```